Quolvex custom business card design

Need a authentic, innovative business card design for a new mobile app business. I am uploading a few screen images from our app for you to view. I would like app design theme to match business card design. I can also send logo images.

```html
<!DOCTYPE html>
<html lang="en">
<head>
<meta charset="utf-8">
<title>Quolvex business card</title>
<link href="https://fonts.googleapis.com/css2?family=Open+Sans:wght@400;600;700;800&display=swap" rel="stylesheet">
<style>
  :root {
    --brand-purple: #5d0391;
    --brand-purple-deep: #4f007c;
    --ink: #1c1c1c;
    --text: #2b2b2b;
    --card-white: #ffffff;
    --page-bg: #e9e9ec;
    --divider: #c9c9c9;
  }
  * { margin: 0; padding: 0; box-sizing: border-box; }
  html, body { width: 1200px; height: 1000px; overflow: hidden; }
  body {
    background: var(--page-bg);
    font-family: "Open Sans", Arial, sans-serif;
    position: relative;
  }
  .card {
    position: absolute;
    left: 270px;
    width: 660px;
    height: 377px;
    box-shadow: 0 6px 18px rgba(0,0,0,0.18);
    overflow: hidden;
  }
  /* Back side */
  .card-back {
    top: 80px;
    background: var(--brand-purple);
  }
  .back-brand {
    position: absolute;
    right: 44px;
    bottom: 52px;
    text-align: right;
    color: var(--card-white);
  }
  .back-brand-name {
    font-weight: 800;
    font-size: 50px;
    line-height: 1;
    letter-spacing: 0.5px;
  }
  .back-brand-url {
    margin-top: 8px;
    font-size: 15px;
    font-weight: 600;
    letter-spacing: 6px;
  }
  /* Front side */
  .card-front {
    top: 520px;
    background: var(--card-white);
  }
  .front-brand {
    position: absolute;
    left: 40px;
    top: 58px;
    width: 240px;
    text-align: center;
  }
  .brand-dot {
    width: 110px;
    height: 110px;
    border-radius: 50%;
    background: var(--brand-purple);
    margin: 0 auto 12px;
  }
  .brand-name {
    font-weight: 800;
    font-size: 46px;
    line-height: 1;
    color: var(--ink);
  }
  .front-divider {
    position: absolute;
    left: 305px;
    top: 60px;
    width: 1px;
    height: 185px;
    background: linear-gradient(to bottom, transparent, var(--divider) 20%, var(--divider) 80%, transparent);
  }
  .contact {
    position: absolute;
    left: 335px;
    top: 62px;
    color: var(--text);
  }
  .contact-name {
    font-weight: 700;
    font-size: 22px;
    color: var(--brand-purple);
    line-height: 1.1;
  }
  .contact-title {
    font-size: 15px;
    letter-spacing: 0.5px;
    margin-bottom: 8px;
  }
  .contact-address {
    font-size: 16px;
    line-height: 1.3;
    margin-bottom: 4px;
  }
  .contact-list { list-style: none; }
  .contact-list li {
    display: flex;
    align-items: center;
    font-size: 16px;
    line-height: 1.45;
  }
  .contact-icon {
    width: 15px;
    height: 15px;
    margin-right: 10px;
    flex: none;
    fill: var(--brand-purple);
  }
  .band {
    position: absolute;
    left: 0;
    right: 0;
    top: 270px;
    height: 44px;
    display: flex;
  }
  .band-web {
    flex: 0 0 540px;
    background: var(--brand-purple);
    color: var(--card-white);
    font-size: 18px;
    letter-spacing: 11px;
    display: flex;
    align-items: center;
    justify-content: center;
  }
  .band-mark {
    flex: 1;
    background: var(--ink);
    position: relative;
  }
  .band-mark-dot {
    position: absolute;
    left: 14px;
    top: 6px;
    width: 32px;
    height: 32px;
    border-radius: 50%;
    background: var(--card-white);
  }
</style>
</head>
<body>

  <section class="card card-back" aria-label="Card back">
    <div class="back-brand">
      <div class="back-brand-name">Quolvex</div>
      <div class="back-brand-url">www.quolvex.com</div>
    </div>
  </section>

  <section class="card card-front" aria-label="Card front">
    <div class="front-brand">
      <div class="brand-dot"></div>
      <div class="brand-name">Quolvex</div>
    </div>

    <div class="front-divider"></div>

    <div class="contact">
      <div class="contact-name">LENA MORO</div>
      <div class="contact-title">PRESIDENT</div>
      <div class="contact-address">4170 Harlow Crest Lane<br>Alder Point, OR 97450</div>
      <ul class="contact-list">
        <li>
          <svg class="contact-icon" viewBox="0 0 16 16" aria-hidden="true"><path d="M1 5c0-2 3-3 7-3s7 1 7 3v1h-4V4.5H5V6H1z M3 7h10l1 7H2z M8 8.5a2 2 0 1 0 0.01 0z"/></svg>
          555 0142 7781
        </li>
        <li>
          <svg class="contact-icon" viewBox="0 0 16 16" aria-hidden="true"><path d="M4 0h8a1 1 0 0 1 1 1v14a1 1 0 0 1-1 1H4a1 1 0 0 1-1-1V1a1 1 0 0 1 1-1zm1 2v10h6V2zm3 11a1 1 0 1 0 .01 0z"/></svg>
          555 0186 3390
        </li>
        <li>
          <svg class="contact-icon" viewBox="0 0 16 16" aria-hidden="true"><path d="M4 1h8v4H4z M1 6h14v7H1z M4 11h8v4H4z"/></svg>
          555 0127 6045
        </li>
        <li>
          <svg class="contact-icon" viewBox="0 0 16 16" aria-hidden="true"><path d="M0 3h16v10H0z M1 4l7 5 7-5" stroke="#fff" stroke-width="1.2"/></svg>
          lena@quolvex.com
        </li>
      </ul>
    </div>

    <div class="band">
      <div class="band-web">www.quolvex.com</div>
      <div class="band-mark"><span class="band-mark-dot"></span></div>
    </div>
  </section>

</body>
</html>
```